Web Design for Palmwick Organic Soap Company

We need a website design for the company Velm Botanics based on the package design per attached.

The design should communicate high end, luxury organic. The site will provide facts about how the spread of disease causes deaths and can be prevented with hand washing. The site will also have a page about why we are passionate about organics and how that relates to our skin including skin facts.
Also, the site should have an e-commerce product page and shopping cart.

Target Market(s)

Educated, health conscious and socially conscious consumers who shop luxury. Target vendors include Tarrow Market and Bellquist..

Industry/Entity Type

E-Commerce

Font styles to use
Other font styles liked:
• See attached

Requirements
Must have
• Use of Ying Yang leaf Logo provided.
Based on design provided.

```html
<!DOCTYPE html>
<html lang="en">
<head>
<meta charset="utf-8">
<title>Velm Botanics — Organic Soap</title>
<link rel="stylesheet" href="https://fonts.googleapis.com/css2?family=Barlow:wght@400;500;600&family=Share+Tech+Mono&display=swap">
<style>
  :root {
    --page: #f4f4f4;
    --panel: #ffffff;
    --ink: #2a2a2a;
    --muted: #555555;
    --rule: #8a8a8a;
    --light-rule: #dcdcdc;
    --green: #6c9a0f;
    --green-dark: #4d7a00;
    --green-box: rgba(110, 155, 15, 0.92);
    --red: #c41010;
    --red-box: rgba(196, 10, 10, 0.92);
    --price: #d01414;
    --logo-ink: #2f3a1d;
  }
  * { margin: 0; padding: 0; box-sizing: border-box; }
  html, body { width: 1023px; height: 1200px; overflow: hidden; }
  body {
    position: relative;
    background: var(--page);
    font-family: "Barlow", Arial, sans-serif;
    color: var(--ink);
  }
  .abs { position: absolute; }

  /* header */
  .sky-scene {
    left: 460px; top: 0; width: 563px; height: 132px;
    background: linear-gradient(180deg, #bcd9ef 0%, #dcebf3 45%, #e6efd8 75%, rgba(244,244,244,0) 100%);
  }
  .brand { left: 85px; top: 13px; display: flex; align-items: center; gap: 10px; }
  .brand-mark { width: 53px; height: 81px; background: var(--green); }
  .brand-name { font-size: 34px; font-weight: 400; color: var(--logo-ink); letter-spacing: 0.5px; }

  .main-nav {
    left: 85px; top: 125px; width: 853px; height: 38px;
    border-top: 1px solid var(--rule); border-bottom: 1px solid var(--rule);
    background: linear-gradient(90deg, #fafafa 0%, #f0f0f0 100%);
  }
  .main-nav a {
    position: absolute; top: 10px; font-size: 13.5px; color: var(--ink);
    text-decoration: none; letter-spacing: 0.6px;
  }
  .main-nav .active::before {
    content: ""; position: absolute; left: -17px; top: -11px; width: 75px; height: 3px; background: var(--green);
  }

  /* sidebar */
  .side-panel { left: 85px; width: 222px; background: var(--panel); border-top: 1px solid var(--green); }
  .side-title {
    height: 37px; padding: 11px 14px 0; font-size: 13px; color: var(--ink);
    border-bottom: 3px double var(--green); background: #f7f7f7;
  }
  .cart-panel { top: 186px; height: 198px; }
  .cart-row { margin: 0 14px; padding: 0 3px; font-size: 10.5px; color: var(--muted); border-bottom: 1px solid var(--light-rule); }
  .cart-row strong { color: var(--green-dark); }
  .btn {
    display: block; width: 115px; height: 36px; border: 1px solid #cfcfcf; background: #f2f2f2; padding: 3px;
  }
  .btn span {
    display: block; height: 100%; background: linear-gradient(180deg, #86b41c, var(--green-dark));
    color: #fff; font-size: 15px; text-align: center; line-height: 28px; font-weight: 500;
  }
  .shop-panel { top: 411px; height: 205px; }
  .shop-list { list-style: none; margin: 6px 14px 0; }
  .shop-list li {
    font-size: 10px; color: var(--muted); padding: 7px 0 7px 15px; border-bottom: 1px solid var(--light-rule); position: relative;
  }
  .shop-list li:last-child { border-bottom: 0; }
  .shop-list li::before {
    content: ""; position: absolute; left: 3px; top: 11px; border-left: 3px solid var(--green); border-top: 2.5px solid transparent; border-bottom: 2.5px solid transparent;
  }
  .video-panel { top: 645px; height: 206px; }
  .video-frame { left: 0; top: 10px; width: 224px; height: 171px; background: linear-gradient(135deg, #6a5a50, #d9c2b0 50%, #7a6a60); }
  .video-bar { left: 6px; bottom: 6px; width: 212px; height: 24px; background: rgba(20,20,20,0.75); }
  .play { left: 10px; top: 6px; border-left: 10px solid #fff; border-top: 6px solid transparent; border-bottom: 6px solid transparent; }
  .shadow { height: 10px; background: radial-gradient(ellipse at top, rgba(0,0,0,0.12), rgba(0,0,0,0) 70%); }

  /* slider */
  .slider { left: 325px; top: 186px; width: 613px; height: 353px; background: var(--panel); border-bottom: 1px solid #cfcfcf; }
  .slide-photo { left: 13px; top: 13px; width: 587px; height: 328px; background: linear-gradient(120deg, #5c4a2e 0%, #a38d5e 35%, #6b6a62 60%, #8b3a22 100%); }
  .release-box { left: 313px; top: 72px; width: 262px; height: 105px; background: var(--green-box); color: #fff; padding: 7px 16px; }
  .release-box h2, .events-box h2 { font-size: 16px; font-weight: 500; letter-spacing: 0.5px; }
  .release-box p { font-size: 9.5px; line-height: 12px; color: #e6f0cf; margin-top: 5px; }
  .release-box a { font-size: 9.5px; color: #111; text-decoration: none; display: block; margin-top: 4px; }
  .events-box { left: 313px; top: 191px; width: 262px; height: 101px; background: var(--red-box); color: #fff; padding: 8px 16px; }
  .events-cols { display: flex; margin-top: 8px; font-family: "Share Tech Mono", monospace; font-size: 9.5px; line-height: 13px; }
  .events-cols div { width: 120px; }
  .events-cols b { font-family: "Barlow", sans-serif; font-size: 11px; font-weight: 600; }
  .dots { left: 876px; top: 545px; display: flex; gap: 6px; }
  .dots i { width: 8px; height: 8px; border-radius: 50%; background: var(--green); }
  .dots i:first-child { background: #fff; }

  /* products */
  .section-title { font-size: 13px; color: var(--ink); }
  .feature-title { left: 325px; top: 570px; width: 613px; height: 24px; padding-left: 13px; border-bottom: 1px solid var(--rule); }
  .products { left: 325px; top: 597px; width: 613px; height: 253px; background: var(--panel); display: flex; }
  .product { width: 153px; border-right: 2px solid #f1f1f1; position: relative; }
  .product:last-child { border-right: 0; }
  .product-photo { position: absolute; left: 16px; top: 18px; width: 132px; height: 99px; border: 1px solid #d6d6d6; background: linear-gradient(160deg, #f7f4ee, #c9a57a 60%, #f4f0ea); }
  .product-name { position: absolute; left: 21px; top: 133px; font-size: 12px; }
  .product-price { position: absolute; left: 21px; top: 161px; font-size: 12px; }
  .product-price b { color: var(--price); font-weight: 500; font-size: 13px; }
  .product .btn { position: absolute; left: 16px; top: 196px; width: 115px; }

  /* about */
  .about-title { left: 86px; top: 877px; width: 852px; height: 26px; padding-left: 12px; border-bottom: 1px solid var(--rule); }
  .about-copy { left: 88px; top: 915px; width: 845px; font-family: "Share Tech Mono", monospace; font-size: 10.6px; line-height: 13.2px; color: #333; }
  .about-list { list-style: none; margin-top: 9px; }
  .about-list li { position: relative; padding-left: 10px; margin-bottom: 7.5px; }
  .about-list li::before {
    content: ""; position: absolute; left: 0; top: 3px; border-left: 3px solid var(--green); border-top: 3px solid transparent; border-bottom: 3px solid transparent;
  }
  .more-info { font-family: "Barlow", sans-serif; font-size: 9px; font-weight: 600; color: var(--green-dark); margin-left: 8px; letter-spacing: 0.5px; }

  .meadow-scene { left: 21px; top: 946px; width: 1002px; height: 180px; background: linear-gradient(180deg, rgba(244,244,244,0) 0%, rgba(225,225,225,0.6) 75%, rgba(244,244,244,0) 100%); }

  /* footer */
  .footer-nav { left: 0; top: 1146px; width: 1023px; text-align: center; font-size: 9.5px; color: #555; letter-spacing: 0.5px; }
  .footer-nav span { margin: 0 6px; }
  .social { left: 0; top: 1173px; width: 1023px; display: flex; justify-content: center; gap: 16px; font-size: 12px; font-weight: 600; color: #111; }
</style>
</head>
<body>

<div class="abs sky-scene" role="img" aria-label="Illustrated sky with clouds and young trees on green hills"></div>

<div class="abs brand">
  <div class="brand-mark"></div>
  <div class="brand-name">Velm Botanics</div>
</div>

<nav class="abs main-nav">
  <a class="active" href="#" style="left:73px">HOME</a>
  <a href="#" style="left:214px">ABOUT</a>
  <a href="#" style="left:351px">CONTACT</a>
  <a href="#" style="left:500px">STORES</a>
  <a href="#" style="left:640px">NATURAL SOAP</a>
</nav>

<!-- sidebar -->
<section class="abs side-panel cart-panel">
  <div class="side-title">Your Shoping</div>
  <div class="cart-row" style="padding-top:17px;padding-bottom:10px">My Cart : <strong>0</strong> products</div>
  <div class="cart-row" style="padding:8px 3px">Organic bar soaps</div>
  <div class="cart-row" style="border:0;padding-top:6px">Total : <strong>$ 0</strong></div>
  <a class="btn" href="#" style="margin:10px 0 0 53px"><span>Details</span></a>
</section>

<section class="abs side-panel shop-panel">
  <div class="side-title">Shop Online</div>
  <ul class="shop-list">
    <li>organic bar soaps</li>
    <li>castile liquid soaps</li>
    <li>organic balms &amp; oils</li>
    <li>unique handmade gifts</li>
    <li>timber &amp; coal for men</li>
  </ul>
</section>

<section class="abs side-panel video-panel">
  <div class="abs video-frame" role="img" aria-label="Video still of a woman washing her face with soap lather">
    <div class="abs video-bar"><div class="abs play"></div></div>
  </div>
</section>

<!-- slider -->
<section class="abs slider">
  <div class="abs slide-photo" role="img" aria-label="Photo of organic soap boxes and balm tins on a table"></div>
  <div class="abs release-box">
    <h2>NEW RELEASES</h2>
    <p>Sed ut perspiciatis unde omnis iste natus error sit voluptatem accusantium doloremque laudantium, totam rem aperiam, eaque ipsa quae ab illo inven-tore</p>
    <a href="#">read more</a>
  </div>
  <div class="abs events-box">
    <h2>UPCOMING EVENTS</h2>
    <div class="events-cols">
      <div><b>when:</b><br>monday,March<br>12th,2014</div>
      <div><b>Location:</b><br>48 Alder Row<br>Fernhaven,CA<br>94017</div>
    </div>
  </div>
</section>
<div class="abs dots"><i></i><i></i><i></i><i></i><i></i></div>

<!-- products -->
<h3 class="abs section-title feature-title">Feature Product</h3>
<section class="abs products">
  <article class="product">
    <div class="product-photo" role="img" aria-label="Two kraft soap boxes"></div>
    <div class="product-name">organic bar soaps</div>
    <div class="product-price">Price : <b>$20</b></div>
    <a class="btn" href="#"><span>Buy</span></a>
  </article>
  <article class="product">
    <div class="product-photo" role="img" aria-label="Two kraft soap boxes"></div>
    <div class="product-name">organic bar soaps</div>
    <div class="product-price">Price : <b>$20</b></div>
    <a class="btn" href="#"><span>Buy</span></a>
  </article>
  <article class="product">
    <div class="product-photo" role="img" aria-label="Two kraft soap boxes"></div>
    <div class="product-name">organic bar soaps</div>
    <div class="product-price">Price : <b>$20</b></div>
    <a class="btn" href="#"><span>Buy</span></a>
  </article>
  <article class="product">
    <div class="product-photo" role="img" aria-label="Two kraft soap boxes"></div>
    <div class="product-name">organic bar soaps</div>
    <div class="product-price">Price : <b>$20</b></div>
    <a class="btn" href="#"><span>Buy</span></a>
  </article>
</section>

<!-- about -->
<div class="abs meadow-scene" role="img" aria-label="Line drawing of a meadow with sprouting plants, rabbits and a windmill"></div>
<h3 class="abs section-title about-title">About</h3>
<div class="abs about-copy">
  <p>Lorem ipsum dolor sit amet, consectetur adipiscing elit. Nulla at dui vitae metus fringilla congue eget et libero. Vivamus lobortis, metus placerat euismod dictum, justo purus eleifend leo, ac imperdiet ipsum dui at mauris.Pellentesque volutpat adipiscing tristique. Nullam varius felis lorem, nec adipiscing nisi. In nisl ipsum, aliquet sit amet auctor nec, facilisis ac dolor. Fusce pulvinar volutpat leo, eu iaculis leo rutrum eu. Nullam ultrices ultrices massa, a sollicitudin elit lobortis eget. Integer id velit. Nam pellentesque scelerisque felis non tempus.</p>
  <ul class="about-list">
    <li>Lorem ipsum dolor sit amet, consectetur adipiscing elit.</li>
    <li>Nulla at dui vitae metus fringilla congue egeteto purus emperdiet ipsum dui at mauris.</li>
    <li>Lorem ipsum dolor sit arus emperdiet ipsuonsectetur adipiscing elit.</li>
  </ul>
  <a class="more-info">- MORE INFO -</a>
</div>

<!-- footer -->
<nav class="abs footer-nav">HOME<span>|</span>ABOUT<span>|</span>CONTACT<span>|</span>STORES<span>|</span>NATURAL SOAP</nav>
<div class="abs social"><span>Kinnet</span><span>Proline</span><span>Reelhall</span></div>

</body>
</html>
```